Brightmark Electrical Flyer

An eye catching flyer design which showcases the type of work we do in the electrical industry in Vancouver,BC. The final design should be simple and incorporate our logo. And present a high end company.

Industry/Entity Type

Electrical

```html
<!DOCTYPE html>
<html lang="en">
<head>
<meta charset="utf-8">
<title>Brightmark Electrical Flyer</title>
<link rel="stylesheet" href="https://fonts.googleapis.com/css2?family=Oswald:wght@400;500;600&family=Exo+2:ital,wght@0,800;0,900;1,900&family=Open+Sans:wght@400;600&display=swap">
<style>
  :root {
    --yellow: #ffd800;
    --yellow-deep: #f2c200;
    --charcoal: #2b2b2b;
    --charcoal-soft: #3a3a3a;
    --ink: #1e1e1e;
    --paper: #f4f4f4;
    --white: #ffffff;
    --stage: #e6e6e6;
  }
  * { box-sizing: border-box; margin: 0; padding: 0; }
  html, body { width: 1200px; height: 1200px; overflow: hidden; background: var(--stage); }
  body { position: relative; font-family: "Open Sans", Arial, sans-serif; }

  .flyer {
    position: absolute; left: 190px; top: 20px;
    width: 820px; height: 1160px;
    background: linear-gradient(180deg, var(--white) 0%, var(--paper) 100%);
    overflow: hidden;
    box-shadow: 0 10px 30px rgba(0,0,0,.18);
  }
  .flyer-shapes { position: absolute; inset: 0; width: 820px; height: 1160px; }

  .headline {
    position: absolute; left: 70px; top: 60px;
    font-family: "Oswald", "Arial Narrow", sans-serif; font-weight: 500;
    line-height: 0.98; text-transform: uppercase;
    transform: rotate(3deg); transform-origin: left top;
  }
  .headline span { display: block; }
  .headline .hl-yellow { color: var(--yellow); }
  .headline .hl-white { color: var(--white); }
  .headline .s1 { font-size: 54px; margin-left: 30px; }
  .headline .s2 { font-size: 48px; margin-left: 18px; }
  .headline .s3 { font-size: 50px; margin-left: 10px; }
  .headline .s4 { font-size: 80px; }
  .headline .s5 { font-size: 54px; margin-left: -6px; }

  .brand {
    position: absolute; right: 40px; top: 150px;
    display: flex; align-items: center; gap: 10px;
    font-family: "Oswald", "Arial Narrow", sans-serif; font-weight: 600;
    font-size: 30px; color: var(--charcoal); letter-spacing: 1px;
  }
  .brand-mark { width: 22px; height: 22px; background: var(--yellow); }

  .tagline {
    position: absolute; left: 60px; top: 430px;
    font-family: "Exo 2", Arial, sans-serif; font-weight: 900; font-style: italic;
    line-height: 0.9; text-transform: uppercase; letter-spacing: 2px;
  }
  .tagline .t1 { display: block; font-size: 76px; color: var(--ink); }
  .tagline .t2 { display: block; font-size: 76px; color: var(--white); margin-left: 20px;
    -webkit-text-stroke: 2px var(--ink); }

  .services-title {
    position: absolute; left: 530px; top: 478px;
    font-family: "Exo 2", Arial, sans-serif; font-weight: 800;
    font-size: 30px; color: var(--white);
  }
  .services-list {
    position: absolute; right: 34px; top: 544px; list-style: none;
    font-family: "Open Sans", Arial, sans-serif; font-size: 19px; color: var(--ink);
    text-align: right; line-height: 1.15;
  }
  .services-list li { display: flex; justify-content: flex-end; align-items: center; gap: 8px; }
  .services-list svg { width: 15px; height: 15px; flex: none; }

  .photo {
    position: absolute; border: 8px solid var(--charcoal);
    box-shadow: 0 6px 14px rgba(0,0,0,.3);
  }
  .photo-lighting { left: 40px; top: 600px; width: 250px; height: 160px;
    background: linear-gradient(90deg, #5a1c10, #e0621d 45%, #ffb545 60%, #8a2a14); }
  .photo-panel { left: 270px; top: 575px; width: 300px; height: 205px;
    background: linear-gradient(90deg, #efe6c8 0%, #e6dcbc 30%, #2d3138 32%, #3c424b 60%, #bfc3c7 62%, #8d9298 100%); }
  .photo-crew { left: 565px; top: 692px; width: 220px; height: 148px;
    background: linear-gradient(135deg, #b08a6a, #d9c28a 40%, #f2c400 55%, #6b5340 100%); }

  .feature { position: absolute; text-align: center; color: var(--ink); }
  .feature h3 {
    font-family: "Oswald", "Arial Narrow", sans-serif; font-weight: 500;
    font-size: 20px; text-transform: uppercase; margin-bottom: 6px; white-space: nowrap;
  }
  .feature p { font-size: 11.5px; line-height: 1.35; }
  .feature-lighting { left: 40px; top: 785px; width: 240px; }
  .feature-panel { left: 290px; top: 805px; width: 260px; }
  .feature-crew { left: 540px; top: 850px; width: 270px; }

  .about { position: absolute; left: 40px; top: 880px; width: 330px; color: var(--ink); }
  .about h2 { font-family: "Exo 2", Arial, sans-serif; font-weight: 900; font-size: 24px; margin-bottom: 6px; }
  .about p { font-size: 14px; line-height: 1.4; }

  .contact {
    position: absolute; left: 455px; top: 960px; width: 340px;
    font-family: "Oswald", "Arial Narrow", sans-serif; color: var(--ink);
    text-transform: uppercase;
  }
  .contact .phone { font-size: 28px; font-weight: 500; white-space: nowrap; }
  .contact .mail { font-size: 18px; font-weight: 500; margin-top: 2px; white-space: nowrap; }

  .footer-join {
    position: absolute; left: 40px; top: 1088px;
    font-size: 20px; color: var(--ink);
  }
  .footer-web {
    position: absolute; right: 40px; top: 1100px;
    font-size: 20px; font-weight: 600; color: var(--white); letter-spacing: .5px;
  }
</style>
</head>
<body>
<article class="flyer">
  <svg class="flyer-shapes" viewBox="0 0 820 1160" aria-hidden="true">
    <defs>
      <linearGradient id="glass" x1="0" y1="0" x2="1" y2="1">
        <stop offset="0" stop-color="#f2f5f8"/>
        <stop offset="0.45" stop-color="#a9bccb"/>
        <stop offset="1" stop-color="#4f667a"/>
      </linearGradient>
      <linearGradient id="charcoal" x1="0" y1="0" x2="1" y2="1">
        <stop offset="0" stop-color="#3d3d3d"/>
        <stop offset="1" stop-color="#222"/>
      </linearGradient>
      <linearGradient id="sun" x1="0" y1="0" x2="1" y2="0">
        <stop offset="0" stop-color="#f5c400"/>
        <stop offset="0.5" stop-color="#ffdf1a"/>
        <stop offset="1" stop-color="#ffd000"/>
      </linearGradient>
    </defs>
    <polygon class="photo-buildings" points="250,0 820,0 820,470 390,410" fill="url(#glass)" role="img" aria-label="Photo of modern glass office towers"/>
    <polygon points="0,0 250,0 390,405 0,370" fill="url(#charcoal)"/>
    <polygon points="250,0 268,0 406,410 390,408" fill="var(--yellow)"/>
    <polygon points="0,385 820,478 820,740 0,720" fill="url(#sun)"/>
    <polygon points="490,462 820,478 820,535 520,520" fill="var(--charcoal)"/>
    <polygon points="0,690 820,720 820,735 0,705" fill="var(--charcoal)"/>
    <polygon points="418,948 800,954 800,1044 462,1040" fill="var(--yellow)"/>
    <polygon points="400,946 420,946 465,1042 445,1042" fill="var(--charcoal)"/>
    <polygon points="0,1050 820,1075 820,1160 0,1160" fill="var(--charcoal)"/>
    <polygon points="0,1058 430,1070 470,1160 0,1160" fill="var(--yellow)"/>
  </svg>

  <h1 class="headline">
    <span class="hl-yellow s1">Expert</span>
    <span class="hl-white s2">Designers</span>
    <span class="hl-yellow s3">Turn your</span>
    <span class="hl-white s4">Dreams</span>
    <span class="hl-yellow s5">Into reality</span>
  </h1>

  <div class="brand"><span class="brand-mark"></span>Brightmark Electrical Inc</div>

  <h2 class="tagline"><span class="t1">Building</span><span class="t2">Dreams</span></h2>

  <div class="services-title">Our Services:</div>
  <ul class="services-list">
    <li>Fire Alarm <svg viewBox="0 0 16 16"><circle cx="8" cy="8" r="7" fill="none" stroke="#1e1e1e" stroke-width="1.4"/><polygon points="5,8 10,5 10,11" fill="#1e1e1e"/></svg></li>
    <li>Security Service <svg viewBox="0 0 16 16"><circle cx="8" cy="8" r="7" fill="none" stroke="#1e1e1e" stroke-width="1.4"/><polygon points="5,8 10,5 10,11" fill="#1e1e1e"/></svg></li>
    <li>Solar Panel <svg viewBox="0 0 16 16"><circle cx="8" cy="8" r="7" fill="none" stroke="#1e1e1e" stroke-width="1.4"/><polygon points="5,8 10,5 10,11" fill="#1e1e1e"/></svg></li>
    <li>Residential lighting <svg viewBox="0 0 16 16"><circle cx="8" cy="8" r="7" fill="none" stroke="#1e1e1e" stroke-width="1.4"/><polygon points="5,8 10,5 10,11" fill="#1e1e1e"/></svg></li>
    <li>Commerical lighting <svg viewBox="0 0 16 16"><circle cx="8" cy="8" r="7" fill="none" stroke="#1e1e1e" stroke-width="1.4"/><polygon points="5,8 10,5 10,11" fill="#1e1e1e"/></svg></li>
    <li>Low Voltage Wiring <svg viewBox="0 0 16 16"><circle cx="8" cy="8" r="7" fill="none" stroke="#1e1e1e" stroke-width="1.4"/><polygon points="5,8 10,5 10,11" fill="#1e1e1e"/></svg></li>
  </ul>

  <div class="photo photo-lighting" role="img" aria-label="Photo of a corridor lit with warm red and amber wall lighting"></div>
  <div class="photo photo-panel" role="img" aria-label="Photo of an electrical smart lighting control panel"></div>
  <div class="photo photo-crew" role="img" aria-label="Photo of an electrician holding a yellow hard hat with a tool belt"></div>

  <div class="feature feature-lighting">
    <h3>Lighting Experts</h3>
    <p>We provide all your lighting needs to complete any project from small to large.</p>
  </div>
  <div class="feature feature-panel">
    <h3>Panelized Smart Lighting</h3>
    <p>Smart lighting solutions give you endless options with your lights</p>
  </div>
  <div class="feature feature-crew">
    <h3>Quality on time construction</h3>
    <p>We efficiently manage construction and coordinate with schedules to always give our clients an effortless experience.</p>
  </div>

  <section class="about">
    <h2>ABOUT US</h2>
    <p>We are an electrical contractor serving the lower mainland. Providing the best in customer service and knowledge, to our clients.</p>
  </section>

  <div class="contact">
    <div class="phone">Contact us at: 778 555 0142</div>
    <div class="mail">Mail us: info@brightmarkelectrical.ca</div>
  </div>

  <div class="footer-join">Join us now for more informations:</div>
  <div class="footer-web">www.brightmarkelectrical.ca</div>
</article>
</body>
</html>
```